Marlowe's Classic Dressing

We are looking for a new label as we switch or glass bottle from a traditional bottle to a round bottle. We want to create a newer/ more appealing logo, while still maintaining some of our old label features to ensure that the brand awareness is not lost. We like the coloring of the blue and white, but feel free to play around with other colors in the design.
We are looking to add product features to our label such as "Gluten-Free", "Original Recipe From 1957" "Family Owned". With this being an older company we would like to keep the traditional feel of our label with some added modern touches.
We are not married to the greek logo/ building but would love some designs with and without it.
WE ARE LOOKING FOR A ROUND LABEL. The pictures provided below are of the old bottle.
There is a picture of the ringneck bottle below. The size of the label is 4.00 x 7.00.

```html
<!DOCTYPE html>
<html lang="en">
<head>
<meta charset="utf-8">
<title>Marlowe's Classic Dressing – Round Label</title>
<link rel="stylesheet" href="https://fonts.googleapis.com/css2?family=Alfa+Slab+One&family=Oswald:wght@500;600;700&display=swap">
<style>
  :root {
    --label-blue: #2b4a9a;
    --rim-blue: #24418a;
    --banner-blue: #3a5cb8;
    --terracotta: #c2602f;
    --terracotta-light: #cf6f45;
    --navy-ink: #23325e;
    --paper: #ffffff;
    --scene-light: #e4e8f5;
    --scene-deep: #a9b6e0;
  }
  html, body {
    margin: 0;
    padding: 0;
    width: 1200px;
    height: 1200px;
    overflow: hidden;
    background: var(--paper);
  }
  .label {
    display: block;
    width: 1200px;
    height: 1200px;
  }
  .rim { fill: var(--paper); stroke: var(--rim-blue); stroke-width: 8; }
  .horizon-rule { stroke: var(--rim-blue); stroke-width: 3; }
  .banner { fill: var(--banner-blue); }
  .banner-underline { stroke: var(--banner-blue); stroke-width: 3; }
  .banner-text {
    font-family: "Oswald", sans-serif;
    font-weight: 600;
    font-size: 44px;
    fill: var(--paper);
  }
  .title-greek {
    font-family: "Alfa Slab One", serif;
    font-size: 124px;
    fill: var(--terracotta);
  }
  .title-dressing {
    font-family: "Oswald", sans-serif;
    font-weight: 700;
    font-size: 164px;
    fill: var(--label-blue);
  }
  .brand-name {
    font-family: "Oswald", sans-serif;
    font-weight: 700;
    font-size: 72px;
    fill: var(--label-blue);
  }
  .claim-gluten {
    font-family: "Oswald", sans-serif;
    font-weight: 500;
    font-size: 66px;
    fill: var(--terracotta-light);
  }
  .claim-family {
    font-family: "Alfa Slab One", serif;
    font-size: 17px;
    fill: var(--label-blue);
  }
  .net-volume {
    font-family: "Oswald", sans-serif;
    font-weight: 600;
    font-size: 25px;
    fill: var(--navy-ink);
  }
</style>
</head>
<body>
<svg class="label" viewBox="0 0 1200 1200" xmlns="http://www.w3.org/2000/svg">
  <defs>
    <clipPath id="label-face">
      <circle cx="604" cy="606" r="402"/>
    </clipPath>
    <linearGradient id="scene-tone" x1="0" y1="0" x2="0" y2="1">
      <stop offset="0" stop-color="var(--scene-light)"/>
      <stop offset="1" stop-color="var(--scene-deep)"/>
    </linearGradient>
  </defs>

  <circle class="rim" cx="604" cy="606" r="405"/>

  <g clip-path="url(#label-face)">
    <rect class="hilltop-scene" x="200" y="245" width="800" height="233"
          fill="url(#scene-tone)" role="img"
          aria-label="Ink illustration of an ancient hilltop citadel with a columned temple"/>
  </g>
  <line class="horizon-rule" x1="222" y1="478" x2="988" y2="478"/>

  <polygon class="banner" points="336,447 872,447 860,503 348,503"/>
  <line class="banner-underline" x1="353" y1="509" x2="856" y2="509"/>
  <text class="banner-text" x="604" y="494" text-anchor="middle"
        textLength="382" lengthAdjust="spacingAndGlyphs">ORIGINAL RECIPE FROM 1957</text>

  <text class="title-greek" x="604" y="614" text-anchor="middle"
        textLength="460" lengthAdjust="spacingAndGlyphs">GREEK</text>
  <text class="title-dressing" x="605" y="749" text-anchor="middle"
        textLength="427" lengthAdjust="spacingAndGlyphs">DRESSING</text>

  <text class="brand-name" x="475" y="900" text-anchor="middle"
        textLength="220" lengthAdjust="spacingAndGlyphs">MARLOWE'S</text>

  <text class="claim-gluten" x="611" y="855"
        textLength="234" lengthAdjust="spacingAndGlyphs">GLUTEN FREE</text>
  <text class="claim-family" x="609" y="888"
        textLength="227" lengthAdjust="spacingAndGlyphs">FAMILY OWNED</text>

  <text class="net-volume" x="601" y="968" text-anchor="middle"
        textLength="134" lengthAdjust="spacingAndGlyphs">8 FL. OZ. 237M</text>
</svg>
</body>
</html>
```